design cheese package for BRUVO

We want someone to give me some graphic designs for the cheese package. You shall not only design it on the basis of our product sizes, but also the design with my company Logo shall be novel and attactive. There are some pictures in the attachments: picture 1--3 for my product; picture 4 for my company Logo; picture 5--6 for your reference Thanks! please add the word BRUVO in the package design, thanks!

Industry/Entity Type

Product

```html
<!DOCTYPE html>
<html lang="en">
<head>
<meta charset="utf-8">
<title>BRUVO Cheese Packages</title>
<link rel="stylesheet" href="https://fonts.googleapis.com/css2?family=Cinzel:wght@700;900&family=Arimo:wght@700&display=swap">
<style>
  :root {
    --backdrop: #e9e3d8;
    --cheese: #f1cd7a;
    --cheese-edge: #e4bd68;
    --olive: #6a7d3c;
    --gold: #f6b41c;
    --gold-ink: #7a7a30;
    --cheddar: #e8322e;
    --mozzarella: #2f7fc6;
    --gouda: #f58a1f;
    --white: #ffffff;
    --ink: #2b2b2b;
  }
  * { box-sizing: border-box; margin: 0; padding: 0; }
  html, body { width: 1200px; height: 900px; overflow: hidden; }
  body { background: var(--backdrop); position: relative; }

  .package {
    position: absolute;
    top: 152px;
    width: 275px;
    height: 595px;
    background: var(--cheese);
    border: 1px solid var(--cheese-edge);
  }
  .package--cheddar { left: 138px; }
  .package--mozzarella { left: 462px; }
  .package--gouda { left: 787px; }

  .label {
    position: absolute;
    left: 24px;
    top: 134px;
    width: 228px;
    height: 342px;
    outline: 3px solid var(--white);
    --variety: var(--cheddar);
  }
  .package--mozzarella .label { --variety: var(--mozzarella); }
  .package--gouda .label { --variety: var(--gouda); }

  .label__art { position: absolute; inset: 0; display: block; }
  .label__art .band-green { fill: var(--olive); }
  .label__art .band-gold { fill: var(--gold); }
  .label__art .field { fill: var(--variety); }
  .label__art .seal { fill: #f4efe1; stroke: var(--white); stroke-width: 2; }
  .label__art .grade {
    font-family: 'Arimo', sans-serif; font-weight: 700; font-size: 9.5px;
    fill: var(--gold-ink); letter-spacing: 0.5px;
  }
  .label__art .flare { fill: var(--white); }
  .label__art .oval { fill: var(--white); }

  .brand {
    position: absolute; left: 0; right: 0; top: 34px;
    text-align: center;
    font-family: 'Arimo', sans-serif; font-weight: 700; font-size: 11px;
    color: var(--olive); letter-spacing: 0.5px;
  }
  .variety-name {
    position: absolute; left: 0; right: 0; top: 138px;
    text-align: center;
    font-family: 'Cinzel', serif; font-weight: 900; font-size: 22px; line-height: 1.05;
    color: var(--white);
  }
  .package--gouda .variety-name { top: 150px; }
  .cheese-word {
    position: absolute; left: 0; right: 0; top: 215px;
    text-align: center;
    font-family: 'Arimo', sans-serif; font-weight: 700; font-size: 14px;
    color: var(--ink);
  }
  .net-weight {
    position: absolute; left: 0; right: 0; top: 303px;
    text-align: center;
    font-family: 'Arimo', sans-serif; font-weight: 700; font-size: 10px; line-height: 1.4;
    color: var(--white);
  }
</style>
</head>
<body>

  <div class="package package--cheddar">
    <div class="label">
      <svg class="label__art" viewBox="0 0 228 342" aria-hidden="true">
        <rect class="band-green" x="0" y="0" width="228" height="342"/>
        <path class="band-gold" d="M0 64 H228 V84 Q150 84 114 110 Q78 84 0 84 Z"/>
        <path class="field" d="M0 84 Q78 84 114 110 Q150 84 228 84 V286 H0 Z"/>
        <rect class="band-gold" x="0" y="286" width="228" height="5"/>
        <circle class="seal" cx="114" cy="38" r="28"/>
        <text class="grade" x="52" y="78" transform="rotate(7 52 78)">CHOICE</text>
        <text class="grade" x="140" y="84" transform="rotate(-7 140 84)">GRADE</text>
        <path class="flare" d="M40 224 L84 222 V226 Z M188 224 L144 222 V226 Z"/>
        <ellipse class="oval" cx="114" cy="224" rx="32" ry="15"/>
      </svg>
      <div class="brand">BRUVO</div>
      <div class="variety-name">MATURED<br>CHEDDAR</div>
      <div class="cheese-word">CHEESE</div>
      <div class="net-weight">NET WT<br>8 OZ (226g)</div>
    </div>
  </div>

  <div class="package package--mozzarella">
    <div class="label">
      <svg class="label__art" viewBox="0 0 228 342" aria-hidden="true">
        <rect class="band-green" x="0" y="0" width="228" height="342"/>
        <path class="band-gold" d="M0 64 H228 V84 Q150 84 114 110 Q78 84 0 84 Z"/>
        <path class="field" d="M0 84 Q78 84 114 110 Q150 84 228 84 V286 H0 Z"/>
        <rect class="band-gold" x="0" y="286" width="228" height="5"/>
        <circle class="seal" cx="114" cy="38" r="28"/>
        <text class="grade" x="52" y="78" transform="rotate(7 52 78)">CHOICE</text>
        <text class="grade" x="140" y="84" transform="rotate(-7 140 84)">GRADE</text>
        <path class="flare" d="M40 224 L84 222 V226 Z M188 224 L144 222 V226 Z"/>
        <ellipse class="oval" cx="114" cy="224" rx="32" ry="15"/>
      </svg>
      <div class="brand">BRUVO</div>
      <div class="variety-name">ITALIAN<br>MOZZARELLA</div>
      <div class="cheese-word">CHEESE</div>
      <div class="net-weight">NET WT<br>8 OZ (226g)</div>
    </div>
  </div>

  <div class="package package--gouda">
    <div class="label">
      <svg class="label__art" viewBox="0 0 228 342" aria-hidden="true">
        <rect class="band-green" x="0" y="0" width="228" height="342"/>
        <path class="band-gold" d="M0 64 H228 V84 Q150 84 114 110 Q78 84 0 84 Z"/>
        <path class="field" d="M0 84 Q78 84 114 110 Q150 84 228 84 V286 H0 Z"/>
        <rect class="band-gold" x="0" y="286" width="228" height="5"/>
        <circle class="seal" cx="114" cy="38" r="28"/>
        <text class="grade" x="52" y="78" transform="rotate(7 52 78)">CHOICE</text>
        <text class="grade" x="140" y="84" transform="rotate(-7 140 84)">GRADE</text>
        <path class="flare" d="M40 224 L84 222 V226 Z M188 224 L144 222 V226 Z"/>
        <ellipse class="oval" cx="114" cy="224" rx="32" ry="15"/>
      </svg>
      <div class="brand">BRUVO</div>
      <div class="variety-name">GOUDA</div>
      <div class="cheese-word">CHEESE</div>
      <div class="net-weight">NET WT<br>8 OZ (226g)</div>
    </div>
  </div>

</body>
</html>
```